Quillmoor Farm Organic Flower Farm, Farmer Florist

I am a flower grower and florist, so I do everything from the field to the vase. I want to include my website, phone, email and instagram

```html
<!DOCTYPE html>
<html lang="en">
<head>
<meta charset="utf-8">
<title>Quillmoor Farm – Business Card Concepts</title>
<link href="https://fonts.googleapis.com/css2?family=Cormorant+Garamond:wght@500&family=Montserrat:wght@400&display=swap" rel="stylesheet">
<style>
  :root{
    --board:#e1e1e1;
    --paper:#ffffff;
    --plum:#5a2a33;
    --wine:#461a21;
    --blush:#f28e8f;
    --sage:#93cc9f;
    --mist:#f1eeef;
    --sprig:#efe9ea;
  }
  *{box-sizing:border-box;margin:0;padding:0}
  html,body{width:1024px;height:1200px;overflow:hidden}
  body{background:var(--board);position:relative;font-family:"Montserrat",sans-serif}
  .card{position:absolute;width:417px;height:238px;background:var(--paper);overflow:hidden}
  .col-left{left:78px}.col-right{left:516px}
  .row-1{top:54px}.row-2{top:325px}.row-3{top:597px}.row-4{top:872px}
  .card-bg{position:absolute;inset:0;width:100%;height:100%}
  .sprig{position:absolute;background:var(--sprig);border-radius:50% 50% 40% 40%/60% 60% 40% 40%;opacity:.8}
  .brand{position:absolute;display:flex;flex-direction:column;align-items:center;transform:translateX(-50%)}
  .brand-dot{width:22px;height:22px;border-radius:50%;background:var(--blush);margin-bottom:10px}
  .brand-dot.sage{background:var(--sage)}
  .brand-name{font-family:"Cormorant Garamond",serif;font-weight:500;color:var(--plum);letter-spacing:.09em;white-space:nowrap;line-height:1}
  .brand.lg .brand-name{font-size:33px}
  .brand.sm .brand-name{font-size:25px}
  .person{position:absolute;font-family:"Cormorant Garamond",serif;font-weight:500;letter-spacing:.03em;white-space:nowrap;line-height:1}
  .role{position:absolute;font-family:"Montserrat",sans-serif;letter-spacing:.04em;white-space:nowrap}
  .contacts{position:absolute;list-style:none;display:flex;flex-direction:column}
  .contacts li{display:flex;align-items:center;gap:7px;font-size:8.3px;white-space:nowrap}
  .ico{width:21px;height:21px;border-radius:50%;display:flex;align-items:center;justify-content:center;flex:none}
  .ico svg{width:11px;height:11px}
  .on-pink li{color:var(--wine)} .on-pink .ico{background:var(--wine)}
  .on-mist li{color:var(--plum)} .on-mist .ico{background:var(--plum)}
  .on-wine li{color:#fff} .on-wine .ico{background:var(--blush)}
</style>
</head>
<body>

<!-- Row 1 -->
<section class="card col-left row-1">
  <div class="sprig" role="img" aria-label="Faint floral sprig illustration" style="left:40px;top:176px;width:340px;height:70px"></div>
  <div class="brand lg" style="left:213px;top:34px">
    <span class="brand-dot"></span>
    <span class="brand-name">QUILLMOOR</span>
  </div>
</section>

<section class="card col-right row-1">
  <div style="position:absolute;left:232px;top:0;width:185px;height:238px;background:var(--blush)"></div>
  <div class="brand sm" style="left:113px;top:56px">
    <span class="brand-dot"></span>
    <span class="brand-name">QUILLMOOR</span>
  </div>
  <div class="person" style="left:259px;top:38px;font-size:18px;color:#fff">TESSA MORROW</div>
  <div class="role" style="left:260px;top:64px;font-size:6.8px;color:#fff">CREATIVE DIRECTOR</div>
  <ul class="contacts on-pink" style="left:260px;top:89px;gap:11px">
    <li><span class="ico"><svg viewBox="0 0 24 24"><path fill="#fff" d="M6.6 10.8a15 15 0 0 0 6.6 6.6l2.2-2.2c.3-.3.7-.4 1-.2 1.1.4 2.3.6 3.6.6.6 0 1 .4 1 1V20c0 .6-.4 1-1 1A17 17 0 0 1 3 4c0-.6.4-1 1-1h3.5c.6 0 1 .4 1 1 0 1.3.2 2.5.6 3.6.1.3 0 .7-.2 1z"/></svg></span>(708) 5550 1427</li>
    <li><span class="ico"><svg viewBox="0 0 24 24"><path fill="#fff" d="M3 6h18v12H3z"/><path fill="none" stroke="var(--wine)" stroke-width="1.8" d="M3 6l9 7 9-7"/></svg></span>hello@quillmoorfarm.com</li>
    <li><span class="ico"><svg viewBox="0 0 24 24" fill="none" stroke="#fff" stroke-width="1.6"><circle cx="12" cy="12" r="9"/><ellipse cx="12" cy="12" rx="4" ry="9"/><path d="M3 12h18M5 7h14M5 17h14"/></svg></span>www.quillmoorfarm.com</li>
    <li><span class="ico"></span>quillmooroninstagram</li>
  </ul>
</section>

<!-- Row 2 -->
<section class="card col-left row-2">
  <div class="sprig" role="img" aria-label="Faint floral sprig illustration" style="left:0;top:0;width:140px;height:60px"></div>
  <div class="sprig" role="img" aria-label="Faint floral sprig illustration" style="left:250px;top:170px;width:167px;height:68px"></div>
  <div class="brand lg" style="left:213px;top:48px">
    <span class="brand-dot sage"></span>
    <span class="brand-name">QUILLMOOR</span>
  </div>
</section>

<section class="card col-right row-2">
  <svg class="card-bg" viewBox="0 0 417 238" preserveAspectRatio="none">
    <path d="M196 0 C232 60 236 160 197 238 L417 238 L417 0 Z" fill="var(--mist)"/>
    <path d="M188 0 C228 50 234 170 203 238" fill="none" stroke="var(--sage)" stroke-width="2.5"/>
  </svg>
  <div role="img" aria-label="Green floral sprig illustration" style="position:absolute;left:0;top:134px;width:162px;height:60px;background:var(--sage);border-radius:10px 60% 30px 40%/20px 60% 20px 50%"></div>
  <div class="person" style="left:21px;top:82px;font-size:22px;color:var(--plum)">TESSA MORROW</div>
  <div class="role" style="left:53px;top:112px;font-size:9.5px;color:var(--sage)">CREATIVE DIRECTOR</div>
  <ul class="contacts on-mist" style="left:253px;top:56px;gap:13px">
    <li><span class="ico"><svg viewBox="0 0 24 24"><path fill="#fff" d="M6.6 10.8a15 15 0 0 0 6.6 6.6l2.2-2.2c.3-.3.7-.4 1-.2 1.1.4 2.3.6 3.6.6.6 0 1 .4 1 1V20c0 .6-.4 1-1 1A17 17 0 0 1 3 4c0-.6.4-1 1-1h3.5c.6 0 1 .4 1 1 0 1.3.2 2.5.6 3.6.1.3 0 .7-.2 1z"/></svg></span>(708) 5550 1427</li>
    <li><span class="ico"><svg viewBox="0 0 24 24"><path fill="#fff" d="M3 6h18v12H3z"/><path fill="none" stroke="var(--plum)" stroke-width="1.8" d="M3 6l9 7 9-7"/></svg></span>hello@quillmoorfarm.com</li>
    <li><span class="ico"><svg viewBox="0 0 24 24" fill="none" stroke="#fff" stroke-width="1.6"><circle cx="12" cy="12" r="9"/><ellipse cx="12" cy="12" rx="4" ry="9"/><path d="M3 12h18M5 7h14M5 17h14"/></svg></span>www.quillmoorfarm.com</li>
    <li><span class="ico"></span>quillmooroninstagram</li>
  </ul>
</section>

<!-- Row 3 -->
<section class="card col-left row-3">
  <div class="sprig" role="img" aria-label="Faint floral sprig illustration" style="left:0;top:140px;width:170px;height:90px"></div>
  <div class="sprig" role="img" aria-label="Faint floral sprig illustration" style="left:247px;top:140px;width:170px;height:90px"></div>
  <div class="brand lg" style="left:213px;top:46px">
    <span class="brand-dot"></span>
    <span class="brand-name">QUILLMOOR</span>
  </div>
</section>

<section class="card col-right row-3">
  <svg class="card-bg" viewBox="0 0 417 238" preserveAspectRatio="none">
    <polygon points="270,0 199,155 262,238 417,238 417,0" fill="var(--blush)"/>
    <polygon points="270,0 208,154 264,238 417,238 417,0" fill="var(--wine)" transform="translate(6 0)"/>
  </svg>
  <div class="sprig" role="img" aria-label="Faint floral sprig illustration" style="left:0;top:176px;width:165px;height:62px"></div>
  <div class="brand sm" style="left:108px;top:52px">
    <span class="brand-dot"></span>
    <span class="brand-name">QUILLMOOR</span>
  </div>
  <ul class="contacts on-wine" style="left:265px;top:68px;gap:11px">
    <li><span class="ico"><svg viewBox="0 0 24 24"><path fill="#fff" d="M6.6 10.8a15 15 0 0 0 6.6 6.6l2.2-2.2c.3-.3.7-.4 1-.2 1.1.4 2.3.6 3.6.6.6 0 1 .4 1 1V20c0 .6-.4 1-1 1A17 17 0 0 1 3 4c0-.6.4-1 1-1h3.5c.6 0 1 .4 1 1 0 1.3.2 2.5.6 3.6.1.3 0 .7-.2 1z"/></svg></span>(708) 5550 1427</li>
    <li><span class="ico"><svg viewBox="0 0 24 24"><path fill="#fff" d="M3 6h18v12H3z"/><path fill="none" stroke="var(--blush)" stroke-width="1.8" d="M3 6l9 7 9-7"/></svg></span>hello@quillmoorfarm.com</li>
    <li><span class="ico"><svg viewBox="0 0 24 24" fill="none" stroke="#fff" stroke-width="1.6"><circle cx="12" cy="12" r="9"/><ellipse cx="12" cy="12" rx="4" ry="9"/><path d="M3 12h18M5 7h14M5 17h14"/></svg></span>www.quillmoorfarm.com</li>
    <li><span class="ico"></span>quillmooroninstagram</li>
  </ul>
</section>

<!-- Row 4 -->
<section class="card col-left row-4">
  <div class="sprig" role="img" aria-label="Faint floral sprig illustration" style="left:40px;top:176px;width:340px;height:62px"></div>
  <div class="brand lg" style="left:213px;top:34px">
    <span class="brand-dot"></span>
    <span class="brand-name">QUILLMOOR</span>
  </div>
</section>

<section class="card col-right row-4">
  <svg class="card-bg" viewBox="0 0 417 238" preserveAspectRatio="none">
    <path d="M322 0 C240 40 200 120 212 200 C214 220 219 230 222 238 L417 238 L417 0 Z" fill="var(--blush)"/>
    <path d="M342 0 C262 40 214 120 224 200 C226 220 229 230 232 238 L417 238 L417 0 Z" fill="#fff"/>
    <path d="M348 0 C268 40 220 120 230 200 C232 220 235 230 238 238 L417 238 L417 0 Z" fill="var(--wine)"/>
  </svg>
  <div class="brand sm" style="left:109px;top:56px">
    <span class="brand-dot"></span>
    <span class="brand-name">QUILLMOOR</span>
  </div>
  <ul class="contacts on-wine" style="left:265px;top:67px;gap:11px">
    <li><span class="ico"><svg viewBox="0 0 24 24"><path fill="#fff" d="M6.6 10.8a15 15 0 0 0 6.6 6.6l2.2-2.2c.3-.3.7-.4 1-.2 1.1.4 2.3.6 3.6.6.6 0 1 .4 1 1V20c0 .6-.4 1-1 1A17 17 0 0 1 3 4c0-.6.4-1 1-1h3.5c.6 0 1 .4 1 1 0 1.3.2 2.5.6 3.6.1.3 0 .7-.2 1z"/></svg></span>(708) 5550 1427</li>
    <li><span class="ico"><svg viewBox="0 0 24 24"><path fill="#fff" d="M3 6h18v12H3z"/><path fill="none" stroke="var(--blush)" stroke-width="1.8" d="M3 6l9 7 9-7"/></svg></span>hello@quillmoorfarm.com</li>
    <li><span class="ico"><svg viewBox="0 0 24 24" fill="none" stroke="#fff" stroke-width="1.6"><circle cx="12" cy="12" r="9"/><ellipse cx="12" cy="12" rx="4" ry="9"/><path d="M3 12h18M5 7h14M5 17h14"/></svg></span>www.quillmoorfarm.com</li>
    <li><span class="ico"></span>quillmooroninstagram</li>
  </ul>
</section>

</body>
</html>
```